Creative Design "Size Chart" for a Clothing Product

Hi, My dear friends! I am looking to do a contest to design a unique creative "Size Chart" for our clothing line. See Attached the Sizes & Ideas Thanks Good Luck Dorian

Colors

Designer to choose colors to be used in the design.

```html
<!DOCTYPE html>
<html lang="en">
<head>
<meta charset="utf-8">
<title>Size Chart</title>
<link rel="stylesheet" href="https://fonts.googleapis.com/css2?family=Saira+Semi+Condensed:wght@400;700;800&display=swap">
<style>
  :root {
    --bg: #ffffff;
    --ink: #0b0b0b;
    --white: #ffffff;
    --header: #399fd8;
    --row-1: #aecdec;
    --row-2: #bad5ef;
    --row-3: #c6dcf1;
    --row-4: #d3e3f4;
    --row-5: #e0eaf6;
    --row-6: #edf3fb;
    --figure-top: #188bca;
    --figure-mid: #0a9ad6;
    --figure-low: #6aaee0;
    --figure-fade: #ffffff;
  }
  * { margin: 0; padding: 0; box-sizing: border-box; }
  html, body { width: 1200px; height: 1200px; overflow: hidden; background: var(--bg); }
  .canvas { position: relative; width: 1200px; height: 1200px; font-family: "Saira Semi Condensed", sans-serif; }
  .figure { position: absolute; left: 156px; top: 331px; width: 281px; height: 544px; }
  .size-table {
    position: absolute; left: 501px; top: 332px; width: 616px;
    border-collapse: collapse; table-layout: fixed;
  }
  .size-table th, .size-table td {
    height: 77.5px; text-align: center; vertical-align: middle; padding: 0;
  }
  .size-table th {
    background: var(--header); color: var(--white);
    font-weight: 800; font-size: 37px; letter-spacing: 0.5px;
  }
  .size-table td { color: var(--ink); font-size: 37px; font-weight: 400; letter-spacing: 2px; }
  .size-table td.size-name { font-weight: 800; letter-spacing: 0.5px; }
  .size-table tr:nth-child(1) td { background: var(--row-1); }
  .size-table tr:nth-child(2) td { background: var(--row-2); }
  .size-table tr:nth-child(3) td { background: var(--row-3); }
  .size-table tr:nth-child(4) td { background: var(--row-4); }
  .size-table tr:nth-child(5) td { background: var(--row-5); }
  .size-table tr:nth-child(6) td { background: var(--row-6); }
  .measure-label { font-family: "Saira Semi Condensed", sans-serif; font-weight: 800; font-size: 28px; fill: var(--white); }
</style>
</head>
<body>
<div class="canvas">
  <svg class="figure" viewBox="0 0 281 544" width="281" height="544">
    <defs>
      <linearGradient id="figureFill" x1="0" y1="0" x2="0" y2="1">
        <stop offset="0" stop-color="var(--figure-top)"/>
        <stop offset="0.4" stop-color="var(--figure-mid)"/>
        <stop offset="0.8" stop-color="var(--figure-low)"/>
        <stop offset="1" stop-color="var(--figure-fade)"/>
      </linearGradient>
    </defs>
    <rect role="img" aria-label="Body silhouette showing where chest and waist are measured" x="0" y="0" width="281" height="544" rx="70" fill="url(#figureFill)"/>
    <g fill="none" stroke="var(--white)" stroke-width="2" stroke-dasharray="6 4">
      <ellipse cx="140" cy="263" rx="71" ry="24"/>
      <ellipse cx="140" cy="343" rx="71" ry="24"/>
    </g>
    <text class="measure-label" x="140" y="273" text-anchor="middle">CHEST</text>
    <text class="measure-label" x="140" y="353" text-anchor="middle">WAIST</text>
  </svg>

  <table class="size-table">
    <thead>
      <tr><th>SIZE</th><th>CHEST</th><th>WAIST</th></tr>
    </thead>
    <tbody>
      <tr><td class="size-name">XXS</td><td>20-23</td><td>19-21</td></tr>
      <tr><td class="size-name">XS</td><td>23-26</td><td>21-23</td></tr>
      <tr><td class="size-name">S</td><td>26-29</td><td>32-25</td></tr>
      <tr><td class="size-name">M</td><td>29-32</td><td>25-27</td></tr>
      <tr><td class="size-name">L</td><td>32-35</td><td>27-29</td></tr>
      <tr><td class="size-name">XL</td><td>35-38</td><td>29-31</td></tr>
    </tbody>
  </table>
</div>
</body>
</html>
```